Home Design company focused on remodel and enhancement of kitchens and bathroorms

I already have a logo designed by ArtHarbor, I now need a design for my business cards.
The company is in the remodeling and enhancement industry for homes, focusing on kitchens and bathrooms, however, we can remodel or enhance every room in a home, an office space, etc.

The company's name is VELMOR HOME DESIGN, LLC

We'll focus on clients in the Rio Grande Valley, Texas. Primarily McAllen, Edinburg, Pharr, Mission, Brownsville and South Padre Island.

The design on the business card should transmit reliability, professionalism anda bit of upscale design.

The logo is in black and white, and would like to keep it that way.

The information that needs to be printed in the business cards is:
Company's name: Velmor Home Design
Company's Logo (attached)
My name: Noel Bramwit
Address, phone and email:
2715 N Parkline Road, Ste 348
Harrowgate, ST 00000
(555) 010 0187
nbramwit@velmordesign.example
Website: velmordesign.example

```html
<!DOCTYPE html>
<html lang="en">
<head>
<meta charset="utf-8">
<title>Velmor Home Design — Business Card</title>
<link rel="stylesheet" href="https://fonts.googleapis.com/css2?family=Montserrat:wght@400;500;800&family=Arimo:wght@400;700&display=swap">
<style>
  :root {
    --ink: #0b0b0b;
    --paper: #f6f6f4;
    --backdrop: #dcdcdc;
    --mark-grey: #c9c9c9;
  }
  * { box-sizing: border-box; margin: 0; padding: 0; }
  html, body { width: 1200px; height: 1200px; overflow: hidden; }
  body {
    background: var(--backdrop);
    display: flex;
    flex-direction: column;
    align-items: center;
    justify-content: center;
    gap: 70px;
    font-family: "Arimo", Arial, sans-serif;
  }
  .card {
    position: relative;
    width: 840px;
    height: 480px;
    background: var(--paper);
    overflow: hidden;
    box-shadow: 0 10px 30px rgba(0,0,0,.18);
  }
  .card.back { background: var(--ink); }
  .card-shapes { position: absolute; inset: 0; width: 100%; height: 100%; }
  .brand {
    position: absolute;
    display: flex;
    align-items: center;
    gap: 14px;
    font-family: "Montserrat", sans-serif;
    font-weight: 500;
    letter-spacing: .28em;
    line-height: 1.15;
    text-transform: uppercase;
    white-space: nowrap;
  }
  .brand-square { width: 14px; height: 14px; background: currentColor; flex: none; }
  .front .brand { left: 40px; top: 205px; color: var(--paper); font-size: 17px; }
  .back .brand { left: 290px; top: 175px; color: var(--mark-grey); font-size: 24px; gap: 18px; }
  .back .brand-square { width: 18px; height: 18px; }
  .holder {
    position: absolute;
    left: 470px; top: 120px;
    font-family: "Montserrat", sans-serif;
    font-weight: 800;
    font-size: 30px;
    letter-spacing: .06em;
    color: var(--ink);
    text-transform: uppercase;
    white-space: nowrap;
  }
  .contacts {
    position: absolute;
    left: 470px; top: 190px;
    list-style: none;
    font-size: 17px;
    color: var(--ink);
  }
  .contacts li { display: flex; align-items: center; gap: 10px; margin-bottom: 10px; white-space: nowrap; }
  .contacts svg, .address svg { width: 18px; height: 18px; flex: none; }
  .address {
    position: absolute;
    left: 560px; top: 345px;
    display: flex; align-items: center; gap: 10px;
    font-style: normal;
    font-size: 17px; font-weight: 700; line-height: 1.25;
    color: var(--paper);
    white-space: nowrap;
  }
</style>
</head>
<body>

<section class="card front" aria-label="Business card front">
  <svg class="card-shapes" viewBox="0 0 840 480" aria-hidden="true">
    <polygon points="0,0 340,0 240,480 0,480" fill="var(--ink)"/>
    <polygon points="282,0 306,0 262,130 238,130" fill="var(--paper)"/>
    <polygon points="212,270 236,270 168,480 144,480" fill="var(--paper)"/>
    <polygon points="240,480 440,300 640,480" fill="var(--ink)"/>
    <polygon points="480,330 840,330 840,420 580,420" fill="var(--ink)"/>
  </svg>

  <div class="brand"><span class="brand-square"></span><span>Velmor<br>Home<br>Design</span></div>

  <h1 class="holder">Noel Bramwit</h1>

  <ul class="contacts">
    <li>
      <svg viewBox="0 0 24 24"><path fill="var(--ink)" d="M6.6 10.8a15 15 0 0 0 6.6 6.6l2.2-2.2c.3-.3.7-.4 1-.2 1.1.4 2.3.6 3.6.6.6 0 1 .4 1 1V20c0 .6-.4 1-1 1A17 17 0 0 1 3 4c0-.6.4-1 1-1h3.5c.6 0 1 .4 1 1 0 1.3.2 2.5.6 3.6.1.3 0 .7-.2 1z"/></svg>
      (555) 010 0187
    </li>
    <li>
      <svg viewBox="0 0 24 24" fill="none" stroke="var(--ink)" stroke-width="2"><circle cx="12" cy="12" r="9"/><ellipse cx="12" cy="12" rx="4" ry="9"/><line x1="3" y1="12" x2="21" y2="12"/></svg>
      www.velmordesign.example
    </li>
    <li>
      <svg viewBox="0 0 24 24"><rect x="2" y="5" width="20" height="14" fill="var(--ink)"/><polyline points="2,5 12,13 22,5" fill="none" stroke="var(--paper)" stroke-width="1.6"/></svg>
      nbramwit@velmordesign.example
    </li>
  </ul>

  <address class="address">
    <svg viewBox="0 0 24 24"><path fill="var(--paper)" d="M12 2a7 7 0 0 0-7 7c0 5 7 13 7 13s7-8 7-13a7 7 0 0 0-7-7zm0 9.5A2.5 2.5 0 1 1 12 6.5a2.5 2.5 0 0 1 0 5z"/></svg>
    <span>2715 N Parkline Road, Ste 348<br>Harrowgate, ST 00000</span>
  </address>
</section>

<section class="card back" aria-label="Business card back">
  <svg class="card-shapes" viewBox="0 0 840 480" aria-hidden="true">
    <polygon points="760,0 784,0 740,150 716,150" fill="var(--paper)"/>
    <polygon points="130,330 154,330 110,480 86,480" fill="var(--paper)"/>
    <polygon points="690,360 714,360 680,480 656,480" fill="var(--paper)"/>
  </svg>
  <div class="brand"><span class="brand-square"></span><span>Velmor<br>Home<br>Design</span></div>
</section>

</body>
</html>
```